Grafic Ad for a Printmagazine about Tractor Vehicles

We need for a Geman Printmagazine about Tractors a Grafic Design in different sizes. Our Website and corporate Design: https://www.kalnoxi.de You can work with the uploaded files . The round Logo with shaking hands should be included in your Designs somehow. Perhaps as a transparent in the background or placed in a corner. The Font used for the URL is Days (glyphvane.com/days.font) Please use this Font or a other similar for the URL "kalnoxi.de" and expand it to "www.kalnoxi.de/traktorwert" For the other Text parts (first line) and (second line) you can use a other font which you prefer. We need the grafics as .jpg in the pixel sizes: 472x496, 437x614, 307x437 (Print would be DPI 300). Goal is a eye-catching design for the later print ad. Have fun and be creative ;)

Logo Text

"Traktor Bewertung" (first line), " Kurzgutachen für Verkauf, Kauf oder Versicherung" (second line), "www.kalnoxi.de/traktorwert" (third line)

Logo styles of interest
Pictorial/Combination Logo
Other font styles liked:
• Days.tff for the URL

Colors
0054AA
0677BA
7BADD7
CADEEF
E8F1F8
0094D4
00A9DD
6FCCEA
C7EBF8
E9F6FB

```html
<!DOCTYPE html>
<html lang="de">
<head>
<meta charset="utf-8">
<title>Traktor Bewertung – Anzeige</title>
<link href="https://fonts.googleapis.com/css2?family=Days+One&display=swap" rel="stylesheet">
<style>
  :root {
    --brand-deep: #0054AA;
    --brand-mid: #0677BA;
    --brand-sky: #0094D4;
    --panel-light: #BDE3FA;
    --panel-tint: #C7EBF8;
    --paper: #FFFFFF;
  }
  html, body {
    margin: 0;
    padding: 0;
    width: 1200px;
    height: 1200px;
    overflow: hidden;
    background: var(--paper);
  }
  .ad-canvas {
    display: block;
    width: 1200px;
    height: 1200px;
  }
  .headline {
    font-family: "Days One", sans-serif;
    fill: var(--paper);
    font-size: 108px;
  }
  .subline {
    font-family: "Days One", sans-serif;
    fill: var(--brand-deep);
    font-size: 54px;
  }
  .url {
    font-family: "Days One", sans-serif;
    fill: var(--paper);
    font-size: 27px;
  }
  .badge-name {
    font-family: "Days One", sans-serif;
    fill: var(--brand-mid);
    font-size: 15px;
  }
</style>
</head>
<body>
<svg class="ad-canvas" viewBox="0 0 1200 1200" xmlns="http://www.w3.org/2000/svg">
  <defs>
    <filter id="soft-shadow" x="-10%" y="-10%" width="120%" height="130%">
      <feDropShadow dx="3" dy="4" stdDeviation="3" flood-color="#00335f" flood-opacity="0.45"/>
    </filter>
    <clipPath id="ad-area">
      <rect x="266" y="230" width="668" height="704"/>
    </clipPath>
  </defs>

  <!-- Ad background -->
  <rect class="ad-background" x="266" y="230" width="668" height="704" fill="var(--brand-mid)"/>
  <rect class="tractor-backdrop" x="266" y="230" width="668" height="704" fill="var(--brand-mid)" opacity="0.9"
        role="img" aria-label="Faint line drawing of a vintage tractor in the background"/>

  <g clip-path="url(#ad-area)">
    <!-- Darker frame behind the info panel -->
    <path class="panel-frame" d="M266 545 L800 486 Q832 484 838 520 L864 718 L266 800 Z" fill="var(--brand-mid)" filter="url(#soft-shadow)"/>

    <!-- Info panel -->
    <path class="info-panel"
          d="M262 569 L792 509 Q826 506 830 540 L848 795 Q850 812 832 814 L262 876 Z"
          fill="var(--panel-light)" stroke="var(--paper)" stroke-width="5" filter="url(#soft-shadow)"/>

    <!-- URL band -->
    <path class="url-band" d="M459 935 L457 900 Q455 872 490 868 L934 814 L934 935 Z" fill="var(--brand-deep)"/>
  </g>

  <!-- Headline -->
  <g class="headline-group" filter="url(#soft-shadow)">
    <text class="headline" x="600" y="356" text-anchor="middle" textLength="606" lengthAdjust="spacingAndGlyphs">TRAKTOR</text>
    <text class="headline" x="600" y="451" text-anchor="middle" textLength="600" lengthAdjust="spacingAndGlyphs">Bewertung</text>
  </g>

  <!-- Subline -->
  <g class="subline-group" transform="rotate(-6 562 680)">
    <text class="subline" x="556" y="612" text-anchor="middle" textLength="372" lengthAdjust="spacingAndGlyphs">Kurzgutachen</text>
    <text class="subline" x="560" y="671" text-anchor="middle" textLength="318" lengthAdjust="spacingAndGlyphs">für Verkauf,</text>
    <text class="subline" x="564" y="730" text-anchor="middle" textLength="266" lengthAdjust="spacingAndGlyphs">Kauf oder</text>
    <text class="subline" x="568" y="789" text-anchor="middle" textLength="356" lengthAdjust="spacingAndGlyphs">Versicherung</text>
  </g>

  <!-- Brand badge -->
  <g class="brand-badge">
    <circle cx="857" cy="766" r="49" fill="var(--paper)" stroke="var(--brand-sky)" stroke-width="6"/>
    <text class="badge-name" x="857" y="771" text-anchor="middle">kalnoxi</text>
  </g>

  <!-- URL -->
  <text class="url" x="688" y="889" text-anchor="middle" textLength="400" lengthAdjust="spacingAndGlyphs"
        transform="rotate(-7.5 688 880)">www.kalnoxi.de/traktorwert</text>
</svg>
</body>
</html>
```